Develop A Dynamic, Professional Powerpoint Design Template

We need a dynamic powerpoint design for a new company that designs novel product packaging. We would like to see designs that use the color black and blue. The final design should communicate "change" and "transitions". See attachments for inspiration on graphics that inspire us.

We like these colors:
Black
Blue
Green
Orange

Reason: We need to extend this contest to allow for the inclusion of our final logo design which is expected to be completed tomorrow, 10/28/2015.

Target Market(s)

High end clients.

Industry/Entity Type

It Company

Font styles to use
Serif

Requirements
Must have
• See "example" slides for type of information that we will be presenting. The name of our company is "Larkspur Carton Works". This template will be used for a new company and I attach a logo concept for your consideration.

```html
<!DOCTYPE html>
<html lang="en">
<head>
<meta charset="utf-8">
<title>Larkspur Carton Works – Presentation Template</title>
<link rel="stylesheet" href="https://fonts.googleapis.com/css2?family=Exo+2:wght@600;700;800&family=Arimo:wght@400;700&display=swap">
<style>
  :root {
    --canvas: #555555;
    --white: #ffffff;
    --green-deep: #1f8f2f;
    --green-mid: #5cb82e;
    --green-light: #b5d936;
    --lime: #d9ec3a;
    --yellow: #f4ee1e;
    --brand-green: #3a9c2c;
    --ink: #333333;
    --muted: #777777;
  }
  * { box-sizing: border-box; margin: 0; padding: 0; }
  html, body { width: 845px; height: 1200px; overflow: hidden; }
  body { background: var(--canvas); position: relative; font-family: "Arimo", Arial, sans-serif; }

  .slide { position: absolute; left: 62px; width: 721px; background: var(--white); overflow: hidden; }
  .slide svg.backdrop { position: absolute; inset: 0; width: 100%; height: 100%; }

  /* Title slide */
  .slide--title { top: 76px; height: 496px; }
  .slide--title .heading {
    position: absolute; left: 36px; top: 200px;
    font-family: "Exo 2", Arial, sans-serif; font-weight: 800; font-size: 46px;
    color: var(--white); letter-spacing: 0.5px;
  }
  .slide--title .subheading {
    position: absolute; left: 38px; top: 260px;
    font-family: "Exo 2", Arial, sans-serif; font-weight: 700; font-size: 27px;
    color: var(--yellow);
  }
  .slide--title .intro {
    position: absolute; left: 38px; top: 312px;
    font-size: 18px; line-height: 26px; color: var(--white);
  }
  .presenter {
    position: absolute; left: 598px; top: 385px;
    font-size: 12px; line-height: 15px; color: var(--ink); font-weight: 700;
  }
  .presenter .date { display: block; margin-top: 10px; font-weight: 400; }
  .brand {
    position: absolute; font-family: "Exo 2", Arial, sans-serif; font-weight: 700;
    color: var(--brand-green); white-space: nowrap;
  }
  .slide--title .brand { left: 40px; top: 428px; font-size: 30px; }
  .web { position: absolute; font-size: 11px; color: var(--brand-green); }
  .slide--title .web { right: 24px; top: 470px; }

  /* Content slide */
  .slide--content { top: 626px; height: 514px; }
  .slide--content .heading {
    position: absolute; left: 30px; top: 24px;
    font-family: "Exo 2", Arial, sans-serif; font-weight: 800; font-size: 31px;
    color: var(--white);
  }
  .slide--content .subheading {
    position: absolute; left: 30px; top: 62px;
    font-family: "Exo 2", Arial, sans-serif; font-weight: 700; font-size: 24px;
    color: var(--yellow);
  }
  .slide--content .brand { right: 18px; top: 50px; font-size: 18px; color: var(--white); }
  .slide--content .web { right: 60px; top: 488px; }
  .page-number {
    position: absolute; right: 26px; top: 486px; padding-left: 10px;
    border-left: 1px solid #bbbbbb; font-size: 11px; color: var(--ink);
  }
</style>
</head>
<body>

<section class="slide slide--title">
  <svg class="backdrop" viewBox="0 0 721 496" preserveAspectRatio="none">
    <defs>
      <linearGradient id="titleFill" x1="0" y1="1" x2="1" y2="0">
        <stop offset="0" stop-color="#1f8f2f"/>
        <stop offset="0.5" stop-color="#5cb82e"/>
        <stop offset="1" stop-color="#d9ec3a"/>
      </linearGradient>
    </defs>
    <path d="M0 0H721V370C600 372 520 395 440 420C330 440 150 432 0 428Z" fill="url(#titleFill)" role="img" aria-label="Green backdrop with floating translucent cubes"/>
    <path d="M0 430C150 434 330 442 440 422C520 397 600 376 721 374" fill="none" stroke="#f4ee1e" stroke-width="4"/>
  </svg>
  <h1 class="heading">HEADING HERE</h1>
  <h2 class="subheading">SUBHEADING HERE</h2>
  <p class="intro">Example Slides For New<br>Design PPT Design Template</p>
  <p class="presenter">NAME OF THE<br>PRESENTERE<span class="date">Date : 00 00 00</span></p>
  <p class="brand">Larkspur Carton Works</p>
  <p class="web">www.larkspurcarton.com</p>
</section>

<section class="slide slide--content">
  <svg class="backdrop" viewBox="0 0 721 514" preserveAspectRatio="none">
    <defs>
      <linearGradient id="bandFill" x1="0" y1="1" x2="1" y2="0">
        <stop offset="0" stop-color="#1f8f2f"/>
        <stop offset="0.55" stop-color="#5cb82e"/>
        <stop offset="1" stop-color="#b5d936"/>
      </linearGradient>
    </defs>
    <path d="M0 0H721V82C640 84 590 90 540 100C480 110 300 104 0 100Z" fill="url(#bandFill)" role="img" aria-label="Green header band with translucent cubes"/>
    <path d="M0 102C300 106 480 112 540 102C590 92 640 86 721 84" fill="none" stroke="#f4ee1e" stroke-width="3"/>
  </svg>
  <h1 class="heading">ADD YOUR HEADING HERE</h1>
  <h2 class="subheading">Add your subheading here</h2>
  <p class="brand">Larkspur Carton Works</p>
  <p class="web">www.larkspurcarton.com</p>
  <p class="page-number">01</p>
</section>

</body>
</html>
```